Developer needs a Software blog Design

I need a design for my software blog (I'm a developer). The design should include a homepage for browser and for mobile.

Following is a wireframe: https://sketchgrid.example/kQp7wz.

The sidebar can also include my picture I you think it should.

In the mobile version the about me and subscribe with email should be popup or dropdown.

I'm currently using this: http://tavelkin.inkpage.example/ which I like, but doesn't have all the component I want on the sidebar and I want something unique.

The most importnant is simple, clean and responsive.

Designs that I like:
http://blog.rupolat.example/
http://xwrt.example/layoutbazaar/?theme=fens
http://demo.skinorbit.example/#singularly

Out come should be a psd file with homepage and mobile homepage (and dropdowns variation for the mobile).

Target Market(s)

developers

Industry/Entity Type

Software

Font styles to use
Sans Serif

Requirements
Must have
• clean and simple. responsive. main post area need to be wide enough.

```html
<!DOCTYPE html>
<html lang="en">
<head>
<meta charset="utf-8">
<title>Tavelkin — Token-Based PubSub</title>
<link href="https://fonts.googleapis.com/css2?family=Open+Sans:wght@300;400;600;700&family=Inconsolata:wght@400;500&display=swap" rel="stylesheet">
<style>
  :root{
    --sidebar:#363d48;
    --field:#262b33;
    --field-line:#1d2128;
    --rule:#4a525e;
    --side-text:#a9b0ba;
    --side-strong:#ffffff;
    --page:#ffffff;
    --ink:#3b4149;
    --body:#6e747b;
    --muted:#9aa0a6;
    --code-bg:#f7f8f9;
    --code-line:#e3e5e8;
    --kw:#d0342c;
    --str:#1a6fb5;
    --blue:#2e9fd6;
    --orange:#f0a21e;
  }
  *{box-sizing:border-box;margin:0;padding:0}
  html,body{width:1200px;height:1127px;overflow:hidden}
  body{background:var(--sidebar);font-family:"Open Sans",Arial,sans-serif;position:relative}

  /* Sidebar */
  .sidebar{position:absolute;left:0;top:0;width:421px;height:1127px;color:var(--side-text)}
  .sidebar > *{position:absolute}
  .brand{right:46px;top:52px;font-size:29px;font-weight:700;color:var(--side-strong);letter-spacing:-.5px}
  .field{left:99px;width:276px;height:34px;background:var(--field);border:1px solid var(--field-line);border-radius:3px;
         font-size:11px;color:#8d95a0;padding:0 14px;display:flex;align-items:center;justify-content:space-between}
  .search{top:129px}
  .email{top:266px;font-size:11.5px}
  .heading{right:46px;font-size:15.5px;font-weight:700;color:var(--side-strong);text-transform:uppercase;letter-spacing:.2px}
  .heading.newsletter{top:199px}
  .heading.recent{top:419px}
  .heading.about{top:832px;right:50px}
  .lead{right:46px;top:232px;font-size:11.5px}
  .rule{left:99px;width:276px;height:1px;background:var(--rule)}
  .social{top:333px;display:flex;align-items:center;gap:10px}
  .social .dot{width:55px;height:55px;border-radius:50%}
  .social small{display:block;font-size:11.5px;color:var(--side-strong)}
  .social b{display:block;font-size:16px;font-weight:600}
  .social.chirp{left:99px}.social.chirp .dot{background:var(--blue)}.social.chirp b{color:var(--blue)}
  .social.rss{left:245px}.social.rss .dot{background:var(--orange)}.social.rss b{color:var(--orange)}
  .post{right:46px;width:290px;text-align:right;font-size:11.3px;line-height:20.5px}
  .post .meta{font-size:8.5px;margin-top:5px;display:flex;justify-content:flex-end;gap:14px;align-items:center}
  .post .meta span{display:flex;align-items:center;gap:5px}
  .links{left:231px;top:652px;width:144px;list-style:none}
  .links li{height:38px;border-bottom:1px solid var(--rule);display:flex;justify-content:flex-end;align-items:center;gap:10px;font-size:11.5px}
  .links .mark{width:10px;height:10px;border:1.5px solid var(--side-text);border-radius:2px}
  .about-text{right:160px;top:890px;width:158px;text-align:right;font-size:10.3px;line-height:20.5px}
  .avatar{left:277px;top:888px;width:98px;height:98px;border-radius:50%;background:radial-gradient(circle at 50% 40%,#c9a48a,#6b5a52 60%,#2b2a2c)}
  .copyright{right:46px;top:1037px;text-align:right;font-size:11.5px;line-height:20px;color:#8b929c}

  /* Main column */
  .main{position:absolute;left:421px;top:0;width:680px;height:1127px;background:var(--page)}
  .main > *{position:absolute}
  .hero{left:31px;top:33px;width:618px;height:199px;background:linear-gradient(110deg,#2c3038 0%,#5f6468 45%,#b9b7b2 75%,#dad8d3 100%)}
  .hero .caption{position:absolute;left:0;right:0;bottom:0;height:45px;background:rgba(40,44,50,.72);color:#fff;
                 font-size:14.5px;display:flex;align-items:center;padding-left:21px}
  .hero .arrows{position:absolute;right:10px;bottom:12px;display:flex;gap:2px}
  .hero .arrows span{width:20px;height:20px;background:rgba(255,255,255,.12);display:flex;align-items:center;justify-content:center}
  .title{left:49px;top:258px;font-size:27px;font-weight:400;color:var(--ink)}
  .post-meta{left:51px;top:303px;font-size:12.5px;color:var(--muted);display:flex;gap:20px}
  .post-meta span{display:flex;align-items:center;gap:6px}
  .divider{left:31px;top:340px;width:618px;height:1px;background:#e8eaec}
  .prose{left:42px;width:600px;font-size:11.1px;line-height:22.3px;color:var(--body)}
  .p1{top:358px}.p2{top:447px}.p3{top:514px}.p4{top:906px}
  .code{left:31px;top:573px;width:618px;height:311px;background:var(--code-bg);border:1px solid var(--code-line);border-radius:2px;
        font-family:"Inconsolata",monospace;font-size:12.5px;color:#4d535a}
  .code > div{position:absolute;white-space:pre}
  .code .wide{letter-spacing:3.2px;color:#6b7178}
  .code .brace{font-size:20px;color:#6b7178}
  .kw{color:var(--kw)}.str{color:var(--str)}
  .loader{left:310px;top:993px;width:60px;height:60px}
  .loading{left:0;width:680px;top:1060px;text-align:center;font-size:17px;color:#c4c8cc;font-weight:300}
</style>
</head>
<body>
<aside class="sidebar">
  <div class="brand">Tavelkin</div>
  <div class="field search">Search :
    <svg width="15" height="15" viewBox="0 0 16 16"><circle cx="6.5" cy="6.5" r="5" fill="none" stroke="#8d95a0" stroke-width="2"/><path d="M10.5 10.5l4 4" stroke="#8d95a0" stroke-width="2.4" stroke-linecap="round"/></svg>
  </div>
  <h2 class="heading newsletter">Newsletter Signup</h2>
  <p class="lead">Get our recent updates through your email id :</p>
  <div class="field email">Enter your email id :
    <svg width="14" height="12" viewBox="0 0 14 12"><path d="M1 6h11M7.5 1.5L12 6l-4.5 4.5" fill="none" stroke="#8d95a0" stroke-width="1.6"/></svg>
  </div>
  <div class="social chirp"><span class="dot"></span><div><small>Follow us on</small><b>Chirpline</b></div></div>
  <div class="social rss"><span class="dot"></span><div><small>Subscribe via</small><b>RSS</b></div></div>

  <h2 class="heading recent">Recent Posts</h2>
  <div class="rule" style="top:457px"></div>
  <article class="post" style="top:470px">
    es simplemente el texto de relleno de las imprentas archivos de texto. sido el texto de...
    <div class="meta"><span>◌ 120 Comments</span><span>☐ 82 likes</span></div>
  </article>
  <article class="post" style="top:557px">
    es simplemente el texto de relleno de las imprentas archivos de texto. sido el texto de...
    <div class="meta"><span>◌ 120 Comments</span><span>☐ 82 likes</span></div>
  </article>

  <ul class="links">
    <li>Repoyard <span class="mark"></span></li>
    <li>Chirpline <span class="mark"></span></li>
    <li>Worknet <span class="mark"></span></li>
    <li>Contact me
      <svg width="11" height="11" viewBox="0 0 16 16"><path d="M3 1l3 3-2 2c1 2 4 5 6 6l2-2 3 3-2 2C8 15 1 8 1 3z" fill="#a9b0ba"/></svg>
    </li>
  </ul>

  <h2 class="heading about">About Me</h2>
  <div class="rule" style="top:871px"></div>
  <p class="about-text">Es simplemente el texto de relleno de las imprentas y archivos de texto. Lorem Ipsum ha sido el texto de relleno estándar de las industrias desde...</p>
  <div class="avatar" role="img" aria-label="Portrait photo of the blog author"></div>
  <p class="copyright">Copyright Tavelkin © 2014 •<br>All rights reserved.</p>
</aside>

<main class="main">
  <figure class="hero" role="img" aria-label="Photo of hands at a desk with laptops and a marker">
    <figcaption class="caption">Es simplemente el texto de relleno de las imprentas y archivos de texto.</figcaption>
    <div class="arrows">
      <span><svg width="7" height="10"><path d="M6 1L2 5l4 4" fill="none" stroke="#ccc"/></svg></span>
      <span><svg width="7" height="10"><path d="M1 1l4 4-4 4" fill="none" stroke="#ccc"/></svg></span>
    </div>
  </figure>

  <h1 class="title">Token-Based PubSub</h1>
  <div class="post-meta">
    <span><svg width="14" height="14" viewBox="0 0 14 14"><rect x="1" y="2" width="12" height="11" fill="none" stroke="#b5babf" stroke-width="1.4"/><path d="M1 5h12" stroke="#b5babf" stroke-width="1.4"/></svg>18 days ago</span>
    <span><svg width="16" height="13" viewBox="0 0 16 13"><path d="M1 1h6l7 6-5 5-8-7z" fill="#b5babf"/></svg>DotRelay · PubSub</span>
  </div>
  <div class="divider"></div>

  <p class="prose p1">I recently pushed two new features to both RelayMQ and DotRelay: manual subscriptions and welcome message, both for the XPub socket. In this post, I will explore what we can do with the manual subscriptions feature. The next post will cover the welcome message.</p>
  <p class="prose p2">Neither feature is part of any release of RelayMQ or DotRelay yet, so you will have to compile from the source code to use the new features.</p>
  <p class="prose p3">I will use DotRelay throughout the post, but you can implement the examples using any RelayMQ binding.</p>

  <div class="code">
    <div style="left:36px;top:26px"><span class="kw">using</span> (<span class="kw">var</span> context = RelayContext.Create())</div>
    <div class="brace" style="left:36px;top:54px">{</div>
    <div class="wide" style="left:58px;top:71px">string[] topics = new string[] { <span class="str">"A"</span>, <span class="str">"B"</span>, <span class="str">"C"</span> };</div>
    <div class="wide" style="left:71px;top:93px">Random random = <span class="kw">new</span> Random();</div>
    <div class="brace" style="left:480px;top:100px">}</div>
    <div style="left:36px;top:137px"><span class="kw">using</span> (<span class="kw">var</span> context = RelayContext.Create())</div>
    <div style="left:36px;top:163px;color:#2a2e33">// we only handle subscription requests, unsubscription and any</div>
    <div style="left:36px;top:185px;color:#2a2e33">// other type of messages will be dropped</div>
    <div class="brace" style="left:36px;top:217px">{</div>
    <div class="wide" style="left:58px;top:234px">string[] topics = new string[] { <span class="str">"A"</span>, <span class="str">"B"</span>, <span class="str">"C"</span> };</div>
    <div class="wide" style="left:71px;top:256px">Random random = <span class="kw">new</span> Random();</div>
    <div class="brace" style="left:480px;top:263px">}</div>
  </div>

  <p class="prose p4">As noted in the example, we confirm all subscription requests, but we drop any other type of request. The sub-scriber will not be able to unsubscribe.</p>

  <svg class="loader" viewBox="0 0 60 60" aria-hidden="true">
    <circle cx="36" cy="7" r="6" fill="#d3d6d9"/>
    <circle cx="21" cy="11" r="5.5" fill="#d3d6d9"/>
    <circle cx="12" cy="27" r="5" fill="#d3d6d9"/>
    <circle cx="18" cy="42" r="4.5" fill="#d3d6d9"/>
    <circle cx="33" cy="47" r="4" fill="#d3d6d9"/>
    <circle cx="47" cy="41" r="3.5" fill="#d3d6d9"/>
    <circle cx="52" cy="28" r="3" fill="#d3d6d9"/>
    <circle cx="49" cy="15" r="2.5" fill="#d3d6d9"/>
  </svg>
  <div class="loading">Loading</div>
</main>
</body>
</html>
```